Love pets? Create a veterinary business card that aligns with our new revamped website.

Greetings! We are a five-doctor veterinary hospital that seeks your expertise in designing a new business card that harmonizes with our recently revitalized website: www.lmcr.net. The card should feature our logo, the five doctors, operating hours, contact information, and communicate our purpose and personality.

Contact Information for Business Card

TBA

```html
<!DOCTYPE html>
<html lang="en">
<head>
<meta charset="utf-8">
<title>Laurel Mill Creek Veterinary Hospital – Business Card</title>
<link href="https://fonts.googleapis.com/css2?family=Poppins:wght@300;400;500&family=Lobster+Two:ital,wght@1,700&display=swap" rel="stylesheet">
<style>
  :root {
    --backdrop: #c1c1c1;
    --paper: #ffffff;
    --leaf: #4a8b41;
    --bark: #7a5a24;
    --frame: #a9c8a4;
  }
  * { margin: 0; padding: 0; box-sizing: border-box; }
  html, body { width: 1093px; height: 1200px; overflow: hidden; }
  body { background: var(--backdrop); font-family: "Poppins", sans-serif; position: relative; }

  .card {
    position: absolute; left: 264px; width: 578px; height: 356px;
    border-radius: 26px; overflow: hidden;
  }
  .card--front { top: 226px; background: var(--paper); }
  .card--back { top: 621px; background: var(--leaf); }

  .brand {
    position: absolute; left: 0; right: 0;
    display: flex; align-items: center; justify-content: center; gap: 14px;
  }
  .card--front .brand { top: 34px; color: var(--leaf); }
  .card--back .brand { top: 60px; color: var(--paper); }
  .brand__dot { width: 54px; height: 54px; border-radius: 50%; background: currentColor; flex: none; }
  .brand__name { font-weight: 500; font-size: 30px; line-height: 1.1; }
  .brand__name span { display: block; font-size: 17px; letter-spacing: 1px; }

  .doctors {
    position: absolute; top: 146px; left: 0; right: 0;
    font-family: "Lobster Two", cursive; font-style: italic; font-weight: 700;
    font-size: 21px; line-height: 29px;
  }
  .doctors__grid { display: flex; justify-content: center; }
  .doctors__col { padding: 0 18px; }
  .doctors__col--left { text-align: right; border-right: 1px solid var(--bark); }
  .doctors__col--right { text-align: left; }
  .doctors__single { text-align: center; }
  .doctor__name { color: var(--leaf); }
  .doctor__title { color: var(--bark); }

  .contact-band {
    position: absolute; left: 0; right: 0; top: 250px; bottom: 0;
    background: var(--leaf); color: var(--paper);
    padding: 22px 0 0 39px; font-weight: 400; font-size: 17px;
  }
  .contact-row { display: flex; align-items: center; gap: 10px; height: 31px; }
  .contact-item { display: flex; align-items: center; gap: 4px; }
  .icon { width: 24px; height: 24px; flex: none; }

  .hours {
    position: absolute; left: 22px; top: 194px; width: 545px; height: 127px;
    border: 2px solid var(--frame); color: var(--paper);
  }
  .hours__title, .hours__note {
    position: absolute; left: 50%; transform: translateX(-50%);
    background: var(--leaf); padding: 0 14px; white-space: nowrap; font-size: 17px;
  }
  .hours__title { top: -13px; }
  .hours__note { bottom: -13px; }
  .hours__table {
    position: absolute; top: 30px; font-size: 17px; line-height: 24px; border-collapse: collapse;
  }
  .hours__table--left { left: 29px; }
  .hours__table--right { left: 287px; }
  .hours__table td { padding: 0; }
  .hours__day { width: 47px; }
</style>
</head>
<body>

<section class="card card--front" aria-label="Business card front">
  <div class="brand">
    <div class="brand__dot"></div>
    <div class="brand__name">Laurel Mill Creek<span>VETERINARY HOSPITAL</span></div>
  </div>

  <div class="doctors">
    <div class="doctors__grid">
      <div class="doctors__col doctors__col--left">
        <div><span class="doctor__name">Dan Morrow,</span> <span class="doctor__title">DVM</span></div>
        <div><span class="doctor__name">Jill Aster,</span> <span class="doctor__title">DVM</span></div>
      </div>
      <div class="doctors__col doctors__col--right">
        <div><span class="doctor__name">Rosa Lind,</span> <span class="doctor__title">DVM</span></div>
        <div><span class="doctor__name">Nora Patel,</span> <span class="doctor__title">DVM</span></div>
      </div>
    </div>
    <div class="doctors__single"><span class="doctor__name">Leah Brooks,</span> <span class="doctor__title">DVM</span></div>
  </div>

  <div class="contact-band">
    <div class="contact-row">
      <span class="contact-item">
        <svg class="icon" viewBox="0 0 24 24" fill="none" stroke="#fff" stroke-width="1.3"><circle cx="12" cy="12" r="11"/><path d="M8 7l2 0 1 3-1.5 1a7 7 0 0 0 3.5 3.5l1-1.5 3 1v2c0 1-1 1.5-2 1.5A9 9 0 0 1 6.5 9c0-1 .5-2 1.5-2z"/></svg>
        (555) 210-4830
      </span>
      <span class="contact-item">
        <svg class="icon" viewBox="0 0 24 24" fill="none" stroke="#fff" stroke-width="1.3"><circle cx="12" cy="12" r="11"/><rect x="8.5" y="6" width="7" height="4"/><rect x="6.5" y="10" width="11" height="5" rx="1" fill="#fff"/><rect x="8.5" y="13" width="7" height="5" fill="#4a8b41"/></svg>
        (555) 210-4831
      </span>
      <span class="contact-item">
        <svg class="icon" viewBox="0 0 24 24" fill="none" stroke="#fff" stroke-width="1.3"><circle cx="12" cy="12" r="11"/><rect x="6.5" y="8" width="11" height="8" fill="#fff"/><path d="M6.5 8l5.5 4.5L17.5 8" stroke="#4a8b41"/></svg>
        info@lmcr.net
      </span>
    </div>
    <div class="contact-row">
      <span class="contact-item">
        <svg class="icon" viewBox="0 0 24 24" fill="none" stroke="#fff" stroke-width="1.3"><circle cx="12" cy="12" r="11"/><path d="M12 18.5s-4.5-5-4.5-8a4.5 4.5 0 0 1 9 0c0 3-4.5 8-4.5 8z" fill="#fff"/><circle cx="12" cy="10.5" r="1.6" fill="#4a8b41" stroke="none"/></svg>
        4820 Cedar Hollow Road, Brookdale, TX 75010
      </span>
    </div>
  </div>
</section>

<section class="card card--back" aria-label="Business card back">
  <div class="brand">
    <div class="brand__dot"></div>
    <div class="brand__name">Laurel Mill Creek<span>VETERINARY HOSPITAL</span></div>
  </div>

  <div class="hours">
    <div class="hours__title">HOSPITAL HOURS</div>
    <table class="hours__table hours__table--left">
      <tr><td class="hours__day">Mon</td><td>7:00am – 6:00pm</td></tr>
      <tr><td class="hours__day">Tue</td><td>7:00am – 6:00pm</td></tr>
      <tr><td class="hours__day">Wed</td><td>7:00am – 6:00pm</td></tr>
    </table>
    <table class="hours__table hours__table--right">
      <tr><td class="hours__day">Thu</td><td>7:00am – 6:00pm</td></tr>
      <tr><td class="hours__day">Fri</td><td>7:00am – 6:00pm</td></tr>
      <tr><td class="hours__day">Sat</td><td>8:00am – 12:00pm</td></tr>
    </table>
    <div class="hours__note">Sunday: Closed</div>
  </div>
</section>

</body>
</html>
```